Skin care manufacturer looking for packaging design for new skin care brand.

We need a design and logo for a skin care brand to be sold at retail stores and online in the United States and Europe. The design will be for 1.7oz - 2oz serums that will not have a retail box. The name of the brand is Velora Fen and should be a luxurious brand that is approachable. The brand will consist of 4 face serums - Vitamin C, Collagen, Retinol and Hyaluronic Acid that all contain Dead Sea Minerals. Images shown are for inspiration only. Color of bottles can be varied based on design and bottles can be screen printed or labeled.

```html
<!DOCTYPE html>
<html lang="en">
<head>
<meta charset="utf-8">
<title>Velora Fen — Facial Serum Labels</title>
<link rel="stylesheet" href="https://fonts.googleapis.com/css2?family=Lato:wght@400;700&family=Source+Sans+3:wght@300;400;500&display=swap">
<style>
  :root {
    --page: #ffffff;
    --gold: #a98466;
    --gold-dark: #7a5a45;
    --ink: #1c1c1f;
    --retinol-top: #8eeefb;
    --retinol-bottom: #a8b2fb;
    --retinol-wave: #c4c4f6;
    --collagen-top: #fdb9a8;
    --collagen-bottom: #fbe2cf;
    --collagen-wave: #f3d9c2;
    --vitamin-top: #fcb87a;
    --vitamin-bottom: #fde3a6;
    --vitamin-wave: #f6d89c;
    --hyaluronic-top: #d9c5fb;
    --hyaluronic-bottom: #f2e3f8;
    --hyaluronic-wave: #ead6f0;
  }
  * { box-sizing: border-box; margin: 0; padding: 0; }
  html, body { width: 916px; height: 1200px; overflow: hidden; background: var(--page); }
  .sheet { position: relative; width: 916px; height: 1200px; }

  .label {
    position: absolute;
    width: 331px;
    height: 310px;
    overflow: hidden;
    display: flex;
    flex-direction: column;
    align-items: center;
    font-family: "Source Sans 3", "Lato", sans-serif;
    color: var(--ink);
    text-align: center;
  }
  .label--retinol { background: linear-gradient(180deg, var(--retinol-top), var(--retinol-bottom)); --wave: var(--retinol-wave); }
  .label--collagen { background: linear-gradient(180deg, var(--collagen-top), var(--collagen-bottom)); --wave: var(--collagen-wave); }
  .label--vitamin { background: linear-gradient(180deg, var(--vitamin-top), var(--vitamin-bottom)); --wave: var(--vitamin-wave); }
  .label--hyaluronic { background: linear-gradient(180deg, var(--hyaluronic-top), var(--hyaluronic-bottom)); --wave: var(--hyaluronic-wave); }

  .label__waves {
    position: absolute;
    left: 0; right: 0; bottom: 0;
    height: 100px;
    background: linear-gradient(180deg, rgba(255,255,255,0) 0%, var(--wave) 55%, rgba(255,255,255,0.55) 100%);
    clip-path: polygon(0 5%, 15% 0, 35% 30%, 60% 35%, 80% 10%, 100% 20%, 100% 100%, 0 100%);
  }

  .brand {
    margin-top: 40px;
    display: flex;
    align-items: center;
    gap: 7px;
    font-family: "Lato", sans-serif;
    font-weight: 700;
    font-size: 20px;
    letter-spacing: 1px;
    color: var(--gold-dark);
  }
  .brand__dot { width: 9px; height: 9px; border-radius: 50%; background: var(--gold); }

  .label__line { font-family: "Lato", sans-serif; font-weight: 400; color: var(--gold); letter-spacing: 0.5px; }
  .label__line--top { margin-top: 28px; font-size: 10px; }
  .label__line--main { font-size: 12px; font-weight: 700; margin-top: 1px; }
  .label__claim { margin-top: 7px; font-size: 7px; font-weight: 500; }

  .label__product { margin-top: 24px; font-size: 23px; font-weight: 400; letter-spacing: 0.5px; line-height: 1; }
  .label__minerals { margin-top: 4px; font-size: 8.5px; letter-spacing: 0.5px; color: var(--gold); }
  .label__size { margin-top: 13px; font-size: 7.5px; font-weight: 500; }

  .row-flat .label:nth-child(1) { left: 112px; top: 515px; }
  .row-flat .label:nth-child(2) { left: 457px; top: 515px; }
  .row-flat .label:nth-child(3) { left: 112px; top: 840px; }
  .row-flat .label:nth-child(4) { left: 457px; top: 840px; }

  .row-mini .label {
    height: 445px;
    transform: scale(0.42);
    transform-origin: top left;
    top: 282px;
  }
  .row-mini .label .brand { margin-top: 30px; }
  .row-mini .label__waves { height: 210px; }
  .row-mini .label:nth-child(1) { left: 124px; }
  .row-mini .label:nth-child(2) { left: 300px; }
  .row-mini .label:nth-child(3) { left: 476px; }
  .row-mini .label:nth-child(4) { left: 652px; }
</style>
</head>
<body>
<main class="sheet">
  <section class="row-mini">
    <article class="label label--retinol">
      <div class="label__waves" role="img" aria-label="Fine-line golden wave pattern"></div>
      <div class="brand"><span class="brand__dot"></span>VELORA FEN</div>
      <p class="label__line label__line--top">ANTI-AGING</p>
      <p class="label__line label__line--main">FACIAL SERUM</p>
      <p class="label__claim">Anti-Aging &amp; Smoothing Treatment</p>
      <h2 class="label__product">RETINOL</h2>
      <p class="label__minerals">With Dead Sea Minerals</p>
      <p class="label__size">1.7 oz / 50 ml</p>
    </article>
    <article class="label label--collagen">
      <div class="label__waves" role="img" aria-label="Fine-line golden wave pattern"></div>
      <div class="brand"><span class="brand__dot"></span>VELORA FEN</div>
      <p class="label__line label__line--top">ANTI-AGING</p>
      <p class="label__line label__line--main">FACIAL SERUM</p>
      <p class="label__claim">Firming &amp; Revitalizing Serum</p>
      <h2 class="label__product">COLLAGEN</h2>
      <p class="label__minerals">With Dead Sea Minerals</p>
      <p class="label__size">1.7 oz / 50 ml</p>
    </article>
    <article class="label label--vitamin">
      <div class="label__waves" role="img" aria-label="Fine-line golden wave pattern"></div>
      <div class="brand"><span class="brand__dot"></span>VELORA FEN</div>
      <p class="label__line label__line--top">ANTI-AGING</p>
      <p class="label__line label__line--main">FACIAL SERUM</p>
      <p class="label__claim">Brightening &amp; Antioxidant Defense</p>
      <h2 class="label__product">VITAMIN C</h2>
      <p class="label__minerals">With Dead Sea Minerals</p>
      <p class="label__size">1.7 oz / 50 ml</p>
    </article>
    <article class="label label--hyaluronic">
      <div class="label__waves" role="img" aria-label="Fine-line golden wave pattern"></div>
      <div class="brand"><span class="brand__dot"></span>VELORA FEN</div>
      <p class="label__line label__line--top">ANTI-AGING</p>
      <p class="label__line label__line--main">FACIAL SERUM</p>
      <p class="label__claim">Hydrating &amp; Plumping Formula</p>
      <h2 class="label__product">HYALURONIC ACID</h2>
      <p class="label__minerals">With Dead Sea Minerals</p>
      <p class="label__size">1.7 oz / 50 ml</p>
    </article>
  </section>

  <section class="row-flat">
    <article class="label label--retinol">
      <div class="label__waves" role="img" aria-label="Fine-line golden wave pattern"></div>
      <div class="brand"><span class="brand__dot"></span>VELORA FEN</div>
      <p class="label__line label__line--top">ANTI-AGING</p>
      <p class="label__line label__line--main">FACIAL SERUM</p>
      <p class="label__claim">Anti-Aging &amp; Smoothing Treatment</p>
      <h2 class="label__product">RETINOL</h2>
      <p class="label__minerals">With Dead Sea Minerals</p>
      <p class="label__size">1.7 oz / 50 ml</p>
    </article>
    <article class="label label--collagen">
      <div class="label__waves" role="img" aria-label="Fine-line golden wave pattern"></div>
      <div class="brand"><span class="brand__dot"></span>VELORA FEN</div>
      <p class="label__line label__line--top">ANTI-AGING</p>
      <p class="label__line label__line--main">FACIAL SERUM</p>
      <p class="label__claim">Firming &amp; Revitalizing Serum</p>
      <h2 class="label__product">COLLAGEN</h2>
      <p class="label__minerals">With Dead Sea Minerals</p>
      <p class="label__size">1.7 oz / 50 ml</p>
    </article>
    <article class="label label--vitamin">
      <div class="label__waves" role="img" aria-label="Fine-line golden wave pattern"></div>
      <div class="brand"><span class="brand__dot"></span>VELORA FEN</div>
      <p class="label__line label__line--top">ANTI-AGING</p>
      <p class="label__line label__line--main">FACIAL SERUM</p>
      <p class="label__claim">Brightening &amp; Antioxidant Defense</p>
      <h2 class="label__product">VITAMIN C</h2>
      <p class="label__minerals">With Dead Sea Minerals</p>
      <p class="label__size">1.7 oz / 50 ml</p>
    </article>
    <article class="label label--hyaluronic">
      <div class="label__waves" role="img" aria-label="Fine-line golden wave pattern"></div>
      <div class="brand"><span class="brand__dot"></span>VELORA FEN</div>
      <p class="label__line label__line--top">ANTI-AGING</p>
      <p class="label__line label__line--main">FACIAL SERUM</p>
      <p class="label__claim">Hydrating &amp; Plumping Formula</p>
      <h2 class="label__product">HYALURONIC ACID</h2>
      <p class="label__minerals">With Dead Sea Minerals</p>
      <p class="label__size">1.7 oz / 50 ml</p>
    </article>
  </section>
</main>
</body>
</html>
```